Need Bus charter business website,

I am starting a bus charter business in the near future. I am based in Geelong, Victoria in Australia. I will have a 25 or 28 seater bus that will be used to take people on charted trips. Whether they be to birthday parties, weddings, sporting events, corporate events, mystery trips, going down the Great Ocean Road, or anywhere someone wants. As for colour scheme, I'm leaning towards something blue and grey, but open to anything really that catches my eye. I played around with a basic web design program and made a basic site which I uploaded ( www.kelmoride.com.au) It has things which I wanted to include such as, services I will provide, trip information, contact form etc.

I don't mind if the layout is completely different to my site as it was only a template that was included in the program I used. I would like the overall design to be relatively fluid, not having to back-track a lot to navigate the site.

```html
<!DOCTYPE html>
<html lang="en">
<head>
<meta charset="utf-8">
<title>Bayline Bus Tours</title>
<link href="https://fonts.googleapis.com/css2?family=Merriweather:ital,wght@0,300;0,400;0,700;1,300;1,400;1,700&display=swap" rel="stylesheet">
<style>
:root{
  --blue:#2a5b8c;
  --blue-dark:#1f4e79;
  --cyan:#29b6e6;
  --slate:#4d5356;
  --card:#383c40;
  --footer:#3b3f42;
  --bar:#121212;
  --ink:#333;
  --muted:#666;
  --line:#c9c9c9;
  --white:#fff;
}
*{margin:0;padding:0;box-sizing:border-box}
html,body{width:1200px;height:1000px;overflow:hidden;background:var(--white)}
body{font-family:"Merriweather",Georgia,serif;color:var(--ink);position:relative}
a{color:inherit;text-decoration:none}

.site-header{position:absolute;left:0;top:0;width:1200px;height:53px}
.brand{position:absolute;left:283px;top:9px;display:flex;align-items:center;gap:8px;font-size:17px;font-weight:700;color:#111}
.brand-mark{width:12px;height:12px;background:#111}
.main-nav{position:absolute;left:570px;top:17px;display:flex;gap:17px;font-size:10px;font-weight:300;color:#333}

.hero{position:absolute;left:172px;top:53px;width:800px;height:271px;overflow:hidden}
.hero-photo{position:absolute;inset:0;background:linear-gradient(180deg,#2aa3df 0%,#7fcdf0 42%,#b9dbe6 58%,#d9a778 70%,#e0b98f 100%)}
.hero-banner{position:absolute;left:0;top:0;width:800px;height:271px}
.hero-title{position:absolute;left:140px;top:110px;width:290px;text-align:center;font-size:24px;font-weight:700;font-style:italic;line-height:30px;color:var(--blue-dark)}

.services{position:absolute;left:172px;top:324px;width:800px;height:214px;background:var(--slate);color:var(--white)}
.services h2{position:absolute;top:22px;width:100%;text-align:center;font-size:18px;font-weight:300;letter-spacing:.5px}
.service-card{position:absolute;top:68px;width:116px;height:116px;background:var(--card);text-align:center}
.service-card svg{display:block;margin:12px auto 0}
.service-card h3{font-size:9.5px;font-weight:400;margin-top:6px}
.service-card p{font-size:7px;line-height:10.5px;color:#ddd;padding:0 10px;margin-top:8px;height:32px;overflow:hidden}
.read-more{position:absolute;left:37px;bottom:-8px;width:48px;height:16px;line-height:16px;font-size:7px;color:var(--white);background:var(--blue);transform:skewX(-18deg)}
.read-more span{display:block;transform:skewX(18deg)}

.journeys{position:absolute;left:282px;top:560px;width:290px}
.section-title{font-size:12.5px;font-style:italic;font-weight:400;color:var(--blue-dark)}
.trip{display:flex;gap:9px;margin-top:13px}
.journeys .trip:first-of-type{margin-top:14px}
.trip-photo{width:46px;height:46px;flex:none}
.trip h4{font-size:9px;font-weight:300;color:#222}
.trip h4 b{font-weight:400}
.trip .date{font-size:7px;color:#555;margin-top:1px}
.trip p{font-size:6.4px;line-height:9px;color:#555;margin-top:2px}

.quick-contact{position:absolute;left:628px;top:560px;width:235px}
.quick-contact .intro{font-size:7.8px;font-style:italic;font-weight:300;line-height:13px;color:#666;margin-top:8px}
.form-row{display:flex;gap:6px;margin-top:10px}
.field{position:relative;height:24px;border:1px solid var(--line);font-size:7px;font-style:italic;color:#666;padding:7px 0 0 20px}
.field svg{position:absolute;left:6px;top:7px}
.field-name{width:94px}
.field-email{width:135px}
.field-message{width:235px;height:66px;margin-top:8px}
.submit{display:inline-block;margin-top:9px;height:21px;padding:0 7px;line-height:19px;border:1px solid var(--blue);font-size:7.5px;font-weight:700;color:var(--blue-dark)}

.site-footer{position:absolute;left:172px;top:786px;width:800px;height:189px;background:var(--footer);color:var(--white)}
.footer-brand{position:absolute;left:0;top:18px;width:100%;display:flex;justify-content:center;align-items:center;gap:7px;font-size:13px;font-weight:400}
.footer-brand .brand-mark{width:9px;height:9px;background:var(--white)}
.footer-col h5{font-size:11px;font-weight:400;margin-bottom:8px}
.footer-about{position:absolute;left:110px;top:68px;width:150px}
.footer-about p{font-size:7.3px;line-height:12.5px;color:#eee}
.footer-about .read-more{position:relative;left:4px;bottom:0;display:inline-block;margin-top:8px;width:48px;text-align:center}
.footer-links{position:absolute;left:286px;top:68px}
.footer-links li{list-style:none;font-size:7.3px;line-height:15px;color:#eee}
.footer-news{position:absolute;left:390px;top:68px;width:150px}
.footer-news .note{font-size:6.8px;font-style:italic;color:#eee}
.news-field{position:relative;margin-top:9px;width:148px;height:22px;background:var(--white);color:#666;font-size:7px;font-style:italic;padding:7px 0 0 21px}
.news-field svg{position:absolute;left:7px;top:7px}
.news-submit{display:inline-block;margin-top:9px;height:20px;line-height:18px;padding:0 6px;border:1px solid #777;background:#2c2f31;font-size:7px;color:#ccc}
.footer-offices{position:absolute;left:568px;top:70px;width:140px}
.office{display:flex;gap:5px;margin-bottom:10px}
.office-icon{width:20px;height:20px;border:2px solid var(--cyan);border-radius:50%;flex:none}
.office b{display:block;font-size:7.5px;font-weight:400;color:var(--cyan)}
.office small{display:block;font-size:6px;color:#ddd}
.phone{display:flex;align-items:center;gap:4px;margin-left:25px;font-size:8.5px;color:#ddd}
.social{display:flex;justify-content:space-around;align-items:center;margin:9px 0 0 25px;width:104px;height:16px;border:1px solid #ccc}
.social i{width:6px;height:6px;border-radius:50%;background:var(--cyan)}

.copyright{position:absolute;left:172px;top:975px;width:800px;height:25px;background:var(--bar);color:#ccc;font-size:7px;text-align:center;line-height:25px}
</style>
</head>
<body>

<header class="site-header">
  <a class="brand" href="#"><span class="brand-mark"></span>Bayline Bus Tours</a>
  <nav class="main-nav">
    <a href="#">About Us</a><a href="#">Services</a><a href="#">Trips on Offers</a><a href="#">Book a Trip</a><a href="#">Contact Us</a>
  </nav>
</header>

<section class="hero">
  <div class="hero-photo" role="img" aria-label="Photo of a smiling family with luggage and beach toys beside a white coach on a tropical beach with palm trees"></div>
  <svg class="hero-banner" viewBox="0 0 800 271" aria-hidden="true">
    <polygon points="86,178 160,105 447,105 373,178" fill="#ffffff" opacity=".95"/>
    <polygon points="373,178 447,105 470,105 396,178" fill="#1f4e79" opacity=".85"/>
    <rect x="86" y="178" width="310" height="3" fill="#1f4e79"/>
  </svg>
  <h1 class="hero-title">Bayline Bus Tours is a family run business</h1>
</section>

<section class="services">
  <h2>OUR SERVICES</h2>

  <article class="service-card" style="left:140px">
    <svg width="36" height="26" viewBox="0 0 36 26" aria-hidden="true"><circle cx="13" cy="13" r="10" fill="none" stroke="#fff" stroke-width="3.5"/><circle cx="23" cy="13" r="10" fill="none" stroke="#fff" stroke-width="3.5"/></svg>
    <h3>WEDDING</h3>
    <p>Our comfortable bus can transport your guests to your ceremony on your</p>
    <a class="read-more" href="#"><span>Read More</span></a>
  </article>

  <article class="service-card" style="left:342px">
    <svg width="36" height="34" viewBox="0 0 36 34" role="img" aria-label="Group of people icon"><circle cx="18" cy="6" r="4" fill="#fff"/><circle cx="8" cy="8" r="3.5" fill="#fff"/><circle cx="28" cy="8" r="3.5" fill="#fff"/><rect x="14" y="11" width="8" height="15" rx="3" fill="#fff"/><rect x="4.5" y="12.5" width="7" height="13" rx="3" fill="#fff"/><rect x="24.5" y="12.5" width="7" height="13" rx="3" fill="#fff"/><rect x="2" y="27" width="32" height="5" rx="2" fill="#fff"/></svg>
    <h3>BUCK’S PARTY</h3>
    <p>Whatever you choose to do on your Buck’s Night, there’s a pretty good</p>
    <a class="read-more" href="#"><span>Read More</span></a>
  </article>

  <article class="service-card" style="left:545px">
    <svg width="36" height="34" viewBox="0 0 36 34" role="img" aria-label="Island with palm trees icon"><ellipse cx="18" cy="28" rx="16" ry="5" fill="#fff"/><rect x="16" y="10" width="3" height="18" fill="#fff"/><ellipse cx="17.5" cy="9" rx="11" ry="4" fill="#fff"/></svg>
    <h3>MYSTRY TRIP</h3>
    <p>Lorem ipsum dolor sit amet, consectetur adipisicing elit,</p>
    <a class="read-more" href="#"><span>Read More</span></a>
  </article>
</section>

<section class="journeys">
  <h2 class="section-title">Happy Journey</h2>
  <article class="trip">
    <div class="trip-photo" role="img" aria-label="Photo of a harbour city skyline with an opera house" style="background:linear-gradient(180deg,#9cc3e0,#6f8ea6)"></div>
    <div><h4>Make happy someone with <b>Melbourne</b> Trip</h4><div class="date">Date:25-8-14</div><p>Melbourne is a maze of hidden laneways, opulent bars, exclusive restaurants and off-the-beaten-track boutiques.</p></div>
  </article>
  <article class="trip">
    <div class="trip-photo" role="img" aria-label="Photo of limestone sea stacks along the coast" style="background:linear-gradient(180deg,#8fb5cf,#b9834a)"></div>
    <div><h4>Amazing beauty of nauture <b>12 Apostles</b> Trip</h4><div class="date">Date:25-8-14</div><p>Golden moments can arise at any time in the National Park but it is dusk and dawn that brings the pilgrims</p></div>
  </article>
  <article class="trip">
    <div class="trip-photo" role="img" aria-label="Photo of a crowded beach with turquoise water" style="background:linear-gradient(180deg,#3aa6c9,#d8c7a6)"></div>
    <div><h4>Fun At <b>Aspen Park</b> Trip</h4><div class="date">Date:25-8-14</div><p>Golden moments can arise at any time in the National Park but it is dusk and dawn that brings the pilgrims</p></div>
  </article>
</section>

<section class="quick-contact">
  <h2 class="section-title">Quick Contact</h2>
  <p class="intro">Couldn’t find what you were looking for? Don’t hesitate to contact us withyour enquiry. You can fill out the form below</p>
  <div class="form-row">
    <div class="field field-name"><svg width="8" height="9" viewBox="0 0 8 9" aria-hidden="true"><circle cx="4" cy="2.5" r="2.2" fill="#555"/><path d="M0 9a4 4 0 0 1 8 0z" fill="#555"/></svg>Full name</div>
    <div class="field field-email"><svg width="9" height="7" viewBox="0 0 9 7" aria-hidden="true"><rect width="9" height="7" fill="#555"/><path d="M0 0l4.5 3.5L9 0" stroke="#fff" fill="none"/></svg>Email Address</div>
  </div>
  <div class="field field-message"><svg width="9" height="8" viewBox="0 0 9 8" aria-hidden="true"><ellipse cx="4.5" cy="3.3" rx="4.5" ry="3.3" fill="#555"/><path d="M1.5 5.5L1 8l3-2z" fill="#555"/></svg>Your message here</div>
  <a class="submit" href="#">Submit Now ›</a>
</section>

<footer class="site-footer">
  <div class="footer-brand"><span class="brand-mark"></span>Bayline Bus Tours</div>

  <div class="footer-col footer-about">
    <h5>About Us</h5>
    <p>Bayline Bus Tours is a family run business. We pride ourselves on providing great service and value for money. We know and love the Geelong region and want to explore more of it with you.</p>
    <a class="read-more" href="#"><span>Read More</span></a>
  </div>

  <div class="footer-col footer-links">
    <h5>Quick Links</h5>
    <ul><li>› About Us</li><li>› Services</li><li>› Trips on Offers</li><li>› Book a Trip</li><li>› Contact Us</li></ul>
  </div>

  <div class="footer-col footer-news">
    <h5>Subscribe to our Newsletter</h5>
    <p class="note">Subscribe to new products, services and stuff,</p>
    <div class="news-field"><svg width="9" height="7" viewBox="0 0 9 7" aria-hidden="true"><rect width="9" height="7" fill="#555"/><path d="M0 0l4.5 3.5L9 0" stroke="#fff" fill="none"/></svg>Email Address</div>
    <a class="news-submit" href="#">Submit Now ›</a>
  </div>

  <div class="footer-offices">
    <div class="office"><span class="office-icon"></span><div><b>Victoria Office</b><small>14 Bayview Rd, Geelong, Victoria</small></div></div>
    <div class="office"><span class="office-icon"></span><div><b>Another Office</b><small>14 Bayview Rd, Geelong, Victoria</small></div></div>
    <div class="phone"><svg width="9" height="8" viewBox="0 0 9 8" aria-hidden="true"><path d="M0 2.5C0 1 2 0 4.5 0S9 1 9 2.5L7 3 6.5 2h-4L2 3zM1.5 4h6l1 4h-8z" fill="#29b6e6"/></svg>+1 800 555 0147</div>
    <div class="social" aria-label="Social links"><i></i><i></i><i></i><i></i><i></i></div>
  </div>
</footer>

<div class="copyright">Copyright 2014 Bayline Bus Tours Pty Ltd. ACN : 000 123 456</div>

</body>
</html>
```